Professional individual needs business card design

I need a business card designed for my friend to show their skills and contact details

I would like to see pattern designs with a black foreground and strong look - will submit content specifics but basics are:

NAME SURNAME (large and bold)
Event Manager & MC

Tressel Magazine
The other event I run

phone number - email

```html
<!DOCTYPE html>
<html lang="en">
<head>
<meta charset="utf-8">
<title>Event Manager Business Card</title>
<link rel="stylesheet" href="https://fonts.googleapis.com/css2?family=Lato:wght@300;400&display=swap">
<style>
  :root {
    --card-bg: #111111;
    --ink-bright: #ffffff;
    --ink-soft: #e6e6e6;
    --ink-mid: #a0a0a0;
    --ink-dark: #555555;
  }
  html, body {
    margin: 0;
    padding: 0;
    width: 1200px;
    height: 703px;
    overflow: hidden;
    background: var(--card-bg);
  }
  .card {
    position: relative;
    width: 1200px;
    height: 703px;
    overflow: hidden;
    background: var(--card-bg);
    font-family: "Lato", sans-serif;
    font-weight: 300;
    color: var(--ink-soft);
  }
  .card-art {
    position: absolute;
    inset: 0;
  }
  .holder-name {
    position: absolute;
    right: 36px;
    top: 82px;
    margin: 0;
    font-size: 100px;
    font-weight: 400;
    line-height: 1;
    white-space: nowrap;
    letter-spacing: -1px;
    color: var(--ink-bright);
  }
  .holder-name .surname {
    background: linear-gradient(90deg, var(--ink-mid) 0%, #808080 50%, var(--ink-dark) 100%);
    -webkit-background-clip: text;
    background-clip: text;
    color: transparent;
  }
  .holder-role {
    position: absolute;
    left: 544px;
    top: 192px;
    margin: 0;
    font-size: 61px;
    line-height: 1;
    white-space: nowrap;
    color: var(--ink-soft);
  }
  .contact-list {
    list-style: none;
    margin: 0;
    padding: 0;
  }
  .contact-item {
    position: absolute;
    font-size: 51px;
    line-height: 1;
    white-space: nowrap;
    color: var(--ink-soft);
  }
  .contact-phone   { left: 104px; top: 350px; }
  .contact-email   { left: 107px; top: 432px; }
  .contact-web     { left: 104px; top: 512px; }
  .contact-address { left: 98px;  top: 600px; }
</style>
</head>
<body>
  <div class="card">
    <svg class="card-art" width="1200" height="703" viewBox="0 0 1200 703" aria-hidden="true">
      <defs>
        <linearGradient id="stripe-sheen" x1="0" y1="0" x2="1200" y2="650" gradientUnits="userSpaceOnUse">
          <stop offset="0" stop-color="#2a2a2a"/>
          <stop offset="0.2" stop-color="#8a8a8a"/>
          <stop offset="0.5" stop-color="#e8e8e8"/>
          <stop offset="0.75" stop-color="#8c8c8c"/>
          <stop offset="1" stop-color="#1e1e1e"/>
        </linearGradient>
        <linearGradient id="marker-sheen" x1="0" y1="0" x2="74" y2="0" gradientUnits="userSpaceOnUse">
          <stop offset="0" stop-color="#3a3a3a"/>
          <stop offset="1" stop-color="#d8d8d8"/>
        </linearGradient>
      </defs>
      <g class="diagonal-stripes" stroke="url(#stripe-sheen)" stroke-width="11" fill="none">
        <line x1="0" y1="-24" x2="1200" y2="624"/>
        <line x1="0" y1="12" x2="1200" y2="660"/>
        <line x1="0" y1="48" x2="1200" y2="696"/>
      </g>
      <g class="contact-markers" fill="url(#marker-sheen)">
        <rect x="0" y="371" width="74" height="14"/>
        <rect x="0" y="455" width="74" height="14"/>
        <rect x="0" y="535" width="74" height="14"/>
        <rect x="0" y="621" width="74" height="14"/>
      </g>
    </svg>

    <h1 class="holder-name">NAME <span class="surname">SURNAME</span></h1>
    <p class="holder-role">Event Manager &amp; MC</p>

    <ul class="contact-list">
      <li class="contact-item contact-phone">5821-340-776</li>
      <li class="contact-item contact-email">sam.reid@inbox.com</li>
      <li class="contact-item contact-web">www.eventsrowan.com</li>
      <li class="contact-item contact-address">Calloway Street , Verin 4040</li>
    </ul>
  </div>
</body>
</html>
```